New Card

Photography business
I want a sleek simple card that screams rich and classy. Black/Gold or silver font. No photos or images but would love a new logo When I hand someone my card I want compliments
Updates
My fiancé reminded me in 5 short months my name will change so I have changed my name to Colleen Marwick
Also my BRAND is Lantern Bloom Photography, not my name. Thanks
Industry/Entity Type
Business
Contact Information for Business Card
Lantern Bloom Photography
Colleen Marwick-owner
482 W. Thornbury Rd.
Alder Ridge, NJ 08099
(856)555-0142
colleen@lanternbloomstudio.example
Look and feel
Each slider illustrates characteristics of the customer's brand and the style your logo design should communicate.

```html
<!DOCTYPE html>
<html lang="en">
<head>
<meta charset="utf-8">
<title>Lantern Bloom Photography – Business Card</title>
<link rel="stylesheet" href="https://fonts.googleapis.com/css2?family=Questrial&display=swap">
<style>
  :root {
    --stage: #2b2b2b;
    --card: #262223;
    --gold: #e8951c;
    --gold-soft: #d98a1a;
    --sun: #ffd400;
    --amber: #f59a1f;
  }
  html, body {
    margin: 0;
    padding: 0;
    width: 1200px;
    height: 799px;
    overflow: hidden;
    background: var(--stage);
    font-family: "Questrial", "Century Gothic", sans-serif;
  }
  .canvas {
    position: relative;
    width: 1200px;
    height: 799px;
  }
  .card {
    position: absolute;
    top: 250px;
    width: 520px;
    height: 298px;
    border-radius: 18px;
    background: var(--card);
    box-shadow: 0 18px 40px rgba(0,0,0,0.45);
    overflow: hidden;
    color: var(--gold);
  }
  .card--front { left: 50px; }
  .card--back { left: 630px; }

  .brand-lockup {
    position: absolute;
    left: 0;
    right: 0;
    top: 122px;
    display: flex;
    align-items: center;
    justify-content: center;
    gap: 12px;
  }
  .brand-lockup__dot {
    width: 14px;
    height: 14px;
    border-radius: 50%;
    background: var(--gold);
  }
  .brand-lockup__name {
    font-size: 28px;
    letter-spacing: 0.5px;
    color: var(--gold);
  }

  .back__title {
    position: absolute;
    left: 150px;
    top: 42px;
    font-size: 23px;
    color: var(--gold);
  }
  .back__details {
    position: absolute;
    left: 68px;
    top: 96px;
  }
  .back__role {
    font-size: 11px;
    color: var(--gold-soft);
    margin: 0 0 2px 14px;
  }
  .back__name {
    font-size: 20px;
    margin: 0 0 6px 10px;
  }
  .contact {
    list-style: none;
    margin: 0;
    padding: 0;
    font-size: 14.5px;
    line-height: 19px;
  }
  .contact li {
    display: flex;
    align-items: flex-start;
    gap: 6px;
  }
  .contact svg {
    flex: none;
    width: 11px;
    height: 11px;
    margin-top: 4px;
  }
  .contact__indent { padding-left: 17px; }

  .back__swoosh {
    position: absolute;
    right: 0;
    bottom: 0;
    width: 520px;
    height: 298px;
  }
</style>
</head>
<body>
<main class="canvas">
  <section class="card card--front" aria-label="Card front">
    <div class="brand-lockup">
      <span class="brand-lockup__dot"></span>
      <span class="brand-lockup__name">Lantern Bloom Photography</span>
    </div>
  </section>

  <section class="card card--back" aria-label="Card back">
    <svg class="back__swoosh" viewBox="0 0 520 298" aria-hidden="true">
      <defs>
        <linearGradient id="sunGrad" x1="0" y1="1" x2="1" y2="0">
          <stop offset="0" stop-color="#ffe600"/>
          <stop offset="1" stop-color="#ffbf00"/>
        </linearGradient>
        <linearGradient id="amberGrad" x1="0" y1="1" x2="1" y2="0">
          <stop offset="0" stop-color="#f7a21f"/>
          <stop offset="1" stop-color="#f08a1c"/>
        </linearGradient>
      </defs>
      <path d="M270 298 C 330 268 470 250 520 110 L520 298 Z" fill="url(#sunGrad)"/>
      <path d="M400 298 C 450 275 500 230 520 160 L520 298 Z" fill="url(#amberGrad)"/>
    </svg>

    <div class="back__title">Lantern Bloom Photography</div>

    <div class="back__details">
      <p class="back__role">Owner</p>
      <p class="back__name">Colleen Marwick</p>
      <ul class="contact">
        <li>
          <svg viewBox="0 0 12 12" aria-hidden="true"><circle cx="6" cy="6" r="5.3" fill="none" stroke="currentColor"/><path d="M6 2.8a2 2 0 0 1 2 2c0 1.5-2 4-2 4s-2-2.5-2-4a2 2 0 0 1 2-2z" fill="currentColor"/></svg>
          <span>482 W. Thornbury Rd.</span>
        </li>
        <li>
          <svg viewBox="0 0 12 12" aria-hidden="true"><circle cx="6" cy="6" r="5.3" fill="none" stroke="currentColor"/><path d="M6 2.8a2 2 0 0 1 2 2c0 1.5-2 4-2 4s-2-2.5-2-4a2 2 0 0 1 2-2z" fill="currentColor"/></svg>
          <span>Alder Ridge,</span>
        </li>
        <li class="contact__indent"><span>NJ 08099</span></li>
        <li>
          <svg viewBox="0 0 12 12" aria-hidden="true"><circle cx="6" cy="6" r="5.3" fill="none" stroke="currentColor"/><path d="M4 3.2l1.2 0 .6 1.6-.8.6c.4.9 1 1.5 1.9 1.9l.6-.8 1.6.6 0 1.2c-3 .3-5.4-2.1-5.1-5.1z" fill="currentColor"/></svg>
          <span>(856)555-0142</span>
        </li>
        <li>
          <svg viewBox="0 0 12 12" aria-hidden="true"><circle cx="6" cy="6" r="5.3" fill="none" stroke="currentColor"/><rect x="3" y="4" width="6" height="4.2" fill="none" stroke="currentColor" stroke-width="0.9"/><path d="M3 4l3 2.3L9 4" fill="none" stroke="currentColor" stroke-width="0.9"/></svg>
          <span>colleen@lanternbloomstudio.example</span>
        </li>
      </ul>
    </div>
  </section>
</main>
</body>
</html>
```